Equine Horse Employment site

We need to redesign the layout of Paddock Crew.co.uk

It will offer Job seekers and Employers the place to look for a job, and look for a candidate.

The logical format needs to be improved and the layout must look highly visually appealing.

It needs to be incredibly simple to use and one click access to any part of the site.

The homepage must convey the following

- Log in and register areas
- Current Job Listings
- Current CV's
- Exclusive Service Club button
- Search box to allow simple searching for Jobs or CVs

We need PSD layouts for Homepage, Job listing Page, CV listing Page, Job Profile and CV Profile. This job is for the design of 5 PSD screens.

Generic page for ancillary page such as about, contact and news.

The biggest competitor is StableandTack.com

Please ask us any questions and please be prepared to make changes, as we are very particular.

More work will be provided to the winning designer.

thanks

• It must not look cheap or like a job board, it has to have character and feel friendly, and inviting. Please do not submit poor designs that look like a job board, as they will be rejected instantly.

thanks

```html
<!DOCTYPE html>
<html lang="en">
<head>
<meta charset="utf-8">
<title>PaddockCrew – Equestrian Recruitment Specialists</title>
<link href="https://fonts.googleapis.com/css2?family=Alegreya+SC:wght@700&family=Arimo:ital,wght@0,400;0,700;1,700&family=Playfair+Display:ital,wght@1,700&family=Alegreya+Sans:ital,wght@1,900&family=Nothing+You+Could+Do&display=swap" rel="stylesheet">
<style>
:root{
  --dark:#151515;
  --dark-2:#1d1d1d;
  --red:#c8150f;
  --red-deep:#a30d0a;
  --green:#5e9c0f;
  --green-nav:#7ab51d;
  --green-btn:#3f9a06;
  --text:#4a4a4a;
  --muted:#777;
  --light:#f2f2f2;
  --panel-top:#fafafa;
  --panel-bottom:#d4d4d4;
  --link:#2a63b8;
  --white:#fff;
}
*{box-sizing:border-box;margin:0;padding:0}
html,body{width:1079px;height:1200px;overflow:hidden;background:var(--dark)}
body{font-family:Arimo,Arial,sans-serif;color:var(--text)}
.page{position:absolute;left:0;top:0;width:1280px;height:1423px;transform:scale(.84297);transform-origin:0 0;background:#fff;overflow:hidden}
.abs{position:absolute}

/* header */
.site-header{position:absolute;left:0;top:0;width:1280px;height:135px;background:linear-gradient(#1b1b1b,#101010)}
.brand{position:absolute;left:140px;top:36px}
.brand-name{font-family:"Alegreya SC",Georgia,serif;font-weight:700;font-size:46px;color:var(--green);letter-spacing:-1px;line-height:1}
.brand-tag{font-family:Arimo,Arial,sans-serif;font-style:italic;font-size:10.5px;color:#9a9a9a;letter-spacing:.6px;margin:2px 0 0 72px}
.main-nav{position:absolute;left:591px;top:60px;display:flex;gap:0;font-weight:700;font-style:italic;font-size:16px}
.main-nav a{color:var(--green-nav);text-decoration:none}
.main-nav a.current{color:#9a9a9a}
.main-nav .sep{color:#555;margin:0 13px;font-weight:400}
.nav-caret{position:absolute;left:606px;top:82px}

/* hero */
.hero{position:absolute;left:0;top:135px;width:1280px;height:386px;background:linear-gradient(#d2211a,var(--red) 40%,var(--red-deep))}
.lower-band{position:absolute;left:0;top:521px;width:1280px;height:212px;background:linear-gradient(#ececec,#fff 60%)}
.search-title{position:absolute;left:160px;top:200px;font-family:"Playfair Display",Georgia,serif;font-style:italic;font-weight:700;font-size:38px;color:var(--white);text-shadow:0 2px 3px rgba(0,0,0,.35)}
.tab{position:absolute;top:204px;height:44px;width:97px;border-radius:10px 10px 0 0;background:linear-gradient(#8a8a8a,#5b5b5b);color:#fff;font-weight:700;font-size:18px;text-align:center;line-height:44px;border:1px solid #b0b0b0}
.search-box{position:absolute;left:163px;top:246px;width:497px;height:54px;border-radius:0 14px 16px 16px;background:linear-gradient(#fff,#ececec);box-shadow:0 4px 6px rgba(0,0,0,.35);font-size:14px;color:#444;padding:18px 0 0 26px}
.search-icon{position:absolute;left:608px;top:250px}
.promo{position:absolute;left:714px;top:180px}
.promo-lead{font-family:"Alegreya Sans",Arial,sans-serif;font-style:italic;font-weight:900;font-size:29px;line-height:30px;color:#2a0000}
.promo-sub{font-family:"Alegreya Sans",Arial,sans-serif;font-style:italic;font-weight:900;font-size:23px;line-height:25px;color:#fff;margin-top:8px}
.promo-sponsor{font-family:"Nothing You Could Do",cursive;font-size:17px;color:#f4d6d6;margin-top:4px}

/* panels */
.panel{position:absolute;border-radius:10px;background:linear-gradient(var(--panel-top),#eeeeee 55%,var(--panel-bottom));border:2px solid #c8c8c8;box-shadow:0 2px 4px rgba(0,0,0,.35)}
.panel-title{position:absolute;font-family:"Alegreya SC",Georgia,serif;font-weight:700;font-size:31px;color:var(--green);text-align:center}
.panel-text{position:absolute;font-size:13.5px;line-height:17px;color:#4a4a4a}
.btn{position:absolute;border-radius:12px;color:#fff;font-weight:700;text-align:center;box-shadow:0 2px 3px rgba(0,0,0,.4)}
.btn-green{background:linear-gradient(#52b412,#2e8a02);font-size:17px;height:38px;line-height:38px;border:1px solid #6cc52b}
.btn-dark{background:linear-gradient(#8a8a8a,#3a3a3a 60%,#2a2a2a);font-size:18px;height:37px;line-height:37px;border:1px solid #999}
.art{position:absolute;border-radius:4px}
.field{position:absolute;left:868px;width:234px;height:36px;border-radius:16px;background:linear-gradient(#fff,#ededed);border:1px solid #d0d0d0;box-shadow:inset 0 2px 3px rgba(0,0,0,.12);font-size:14px;padding:9px 0 0 22px;color:#444}
.small-link{position:absolute;top:514px;font-size:11px;color:#444}

/* welcome */
.section-title{position:absolute;font-family:"Alegreya SC",Georgia,serif;font-weight:700;font-size:34px;color:var(--green)}
.welcome-text{position:absolute;left:160px;top:660px;width:625px;font-size:14.5px;line-height:18px;color:#555}
.rule-v{position:absolute;border-left:1px dashed #c8c8c8}
.rule-h{position:absolute;border-top:1px dashed #cfcfcf}
.club-btn{position:absolute;left:819px;top:643px;width:297px;height:46px;border-radius:10px;background:linear-gradient(#8d8d8d,#444 55%,#333);border:1px solid #aaa;box-shadow:0 3px 4px rgba(0,0,0,.4);font-family:"Alegreya Sans",Arial,sans-serif;font-style:italic;font-weight:900;font-size:24px;color:#fff;text-align:center;line-height:44px}

/* listings */
.listings{position:absolute;left:0;top:733px;width:1280px;height:320px;background:linear-gradient(#f0f0f0,#fafafa 40%,#f3f3f3)}
.col-divider{position:absolute;left:748px;top:733px;width:6px;height:320px;background:linear-gradient(90deg,#d6d6d6,#f6f6f6)}
.job{position:absolute;width:270px}
.job h3{font-size:20px;color:#444;font-weight:700}
.job p{font-size:12px;line-height:14px;color:#555;margin-top:4px;height:28px}
.job-meta{display:flex;align-items:center;font-size:12px;color:#555;margin-top:8px}
.job-meta svg{margin-right:6px}
.job-meta .gap{width:18px}
.cv-table{position:absolute;left:775px;top:810px;width:348px;border-collapse:collapse;font-size:12px;background:#fff}
.cv-table th{background:#e1e1e1;text-align:left;font-size:14.5px;color:#444;height:33px;padding-left:7px;border-right:1px solid #fff}
.cv-table td{height:32.5px;padding-left:7px;color:#555;border-right:1px solid #e6e6e6;border-bottom:1px solid #e6e6e6}
.cv-table tr:nth-child(even) td{background:#efefef}
.cv-table td.file{color:var(--link)}
.cv-table td.icon{text-align:center;padding-left:0}

/* partners */
.partners{position:absolute;left:0;top:1053px;width:1280px;height:70px;background:linear-gradient(#f1f1f1,#e3e3e3)}
.partner{position:absolute;top:1080px;font-size:15px;color:#777;font-weight:700;letter-spacing:-.3px}

/* footer */
.site-footer{position:absolute;left:0;top:1123px;width:1280px;height:265px;background:var(--dark-2)}
.foot-title{position:absolute;top:1159px;font-size:20px;font-weight:700;color:#9b9b9b}
.foot-list{position:absolute;list-style:none;font-size:12px;color:#7d7d7d}
.foot-list li{display:flex;align-items:center;height:18px}
.foot-list li svg{margin-right:6px}
.social li{height:20px}
.social .sq{width:15px;height:15px;border-radius:2px;margin-right:7px}
.foot-label{position:absolute;left:358px;top:1208px;font-size:12px;color:#7d7d7d}
.foot-field{position:absolute;left:355px;top:1228px;width:234px;height:36px;border-radius:16px;background:linear-gradient(#e0e0e0,#bdbdbd);font-size:14px;color:#333;padding:10px 0 0 23px}
.quote{position:absolute;left:850px;top:1203px;width:289px;height:137px;border-radius:16px;background:var(--green);color:#fff;font-size:12px;line-height:15.5px;padding:20px 14px 0 18px}
.quote-author{position:absolute;left:890px;top:1349px;font-size:13px;font-weight:700;color:#999}
.copy-bar{position:absolute;left:0;top:1388px;width:1280px;height:35px;background:linear-gradient(#d01d16,#a80e0a);text-align:center;font-size:11px;color:#fff;line-height:35px}
</style>
</head>
<body>
<div class="page">

  <header class="site-header">
    <div class="brand">
      <div class="brand-name">PaddockCrew</div>
      <div class="brand-tag">EQUESTRIAN RECRUITMENT SPECIALISTS</div>
    </div>
    <nav class="main-nav">
      <a class="current" href="#">Home</a><span class="sep">/</span>
      <a href="#">About Us</a><span class="sep">/</span>
      <a href="#">Employers</a><span class="sep">/</span>
      <a href="#">Advertise</a><span class="sep">/</span>
      <a href="#">News</a><span class="sep">/</span>
      <a href="#">Resources</a>
    </nav>
    <svg class="nav-caret" width="14" height="8" viewBox="0 0 14 8"><path d="M0 0h14L7 8z" fill="#8a8a8a"/></svg>
  </header>

  <section class="hero"></section>
  <div class="lower-band"></div>

  <h1 class="search-title">JOB SEARCH</h1>
  <div class="tab" style="left:433px">Jobs</div>
  <div class="tab" style="left:537px">CVs</div>
  <div class="search-box">Enter Keyword</div>
  <svg class="search-icon" width="64" height="64" viewBox="0 0 64 64">
    <line x1="36" y1="36" x2="58" y2="58" stroke="#555" stroke-width="7" stroke-linecap="round"/>
    <circle cx="24" cy="24" r="19" fill="#d8ecf8" stroke="#9a9a9a" stroke-width="4"/>
    <path d="M12 20a13 13 0 0 1 12-9" stroke="#fff" stroke-width="3" fill="none" stroke-linecap="round"/>
  </svg>

  <div class="promo">
    <div class="promo-lead">Unbeatable Job Postings<br>From Just $30</div>
    <div class="promo-sub">Now With Over 1.9 Million Job Views<br>A Week - You're In The Right Place</div>
    <div class="promo-sponsor">Sponsored By Saddle Row Supplies</div>
  </div>

  <!-- seeker / employer panel -->
  <div class="panel" style="left:160px;top:367px;width:680px;height:219px"></div>
  <div class="rule-v" style="left:498px;top:369px;height:215px;border-left:1px solid #cfcfcf"></div>

  <div class="panel-title" style="left:160px;top:385px;width:338px">Job Seeker</div>
  <p class="panel-text" style="left:203px;top:446px;width:200px">Get Recommendations from past employers and stand out from the crowd.</p>
  <div class="art" role="img" aria-label="Framed certificate with a red seal" style="left:414px;top:433px;width:66px;height:87px;background:linear-gradient(#b07a4a,#8a5a32);transform:rotate(6deg)"></div>
  <div class="btn btn-green" style="left:205px;top:535px;width:227px">Sign Up for FREE!</div>

  <div class="panel-title" style="left:498px;top:385px;width:326px">Employer</div>
  <p class="panel-text" style="left:517px;top:446px;width:210px">List jobs starting at $15 for 30 days. Find great employees with recommendations from past employers.</p>
  <div class="art" role="img" aria-label="Approval seal under a magnifying glass" style="left:730px;top:442px;width:108px;height:84px;border-radius:40px 40px 40px 10px;background:linear-gradient(135deg,#8fb6d6,#3b6e9c 60%,#444)"></div>
  <div class="btn btn-green" style="left:557px;top:535px;width:227px">Sign Up!</div>

  <!-- login -->
  <div class="panel" style="left:851px;top:368px;width:267px;height:220px"></div>
  <div class="panel-title" style="left:851px;top:380px;width:267px;font-size:29px">Login</div>
  <div class="field" style="top:422px">Username</div>
  <div class="field" style="top:466px;font-size:12px;padding-top:12px">**********</div>
  <span class="small-link" style="left:874px">Forgot Password?</span>
  <span class="small-link" style="left:1054px">Register</span>
  <div class="btn btn-dark" style="left:868px;top:537px;width:227px">Login</div>

  <!-- welcome -->
  <h2 class="section-title" style="left:160px;top:610px">Welcome to PaddockCrew</h2>
  <p class="welcome-text">Equestrian Jobs at PaddockCrew. A precise way for equine job seekers and employers to conduct a search for qualified candidates and jobs. No1 in Seekly and a reach of over 500,000 users in the UK alone. Now partnered with Hayloft Market providing greater reach to the best talent in Europe.</p>
  <div class="rule-v" style="left:798px;top:625px;height:88px"></div>
  <div class="club-btn">Exclusive Service Club</div>

  <!-- listings -->
  <section class="listings"></section>
  <div class="col-divider"></div>
  <h2 class="section-title" style="left:160px;top:758px">Current Job Listings</h2>
  <div class="rule-v" style="left:433px;top:828px;height:195px"></div>
  <div class="rule-h" style="left:160px;top:925px;width:540px"></div>

  <article class="job" style="left:161px;top:823px">
    <h3>Riding Instructor</h3>
    <p>Part-time riding instructor,to work evenings &amp; weekends</p>
    <div class="job-meta">
      <svg width="14" height="20" viewBox="0 0 14 20"><path d="M7 20C3 14 0 10 0 7a7 7 0 0 1 14 0c0 3-3 7-7 13z" fill="#e0502a"/><circle cx="7" cy="7" r="2.5" fill="#fff"/></svg>Where it is?<span class="gap"></span>
      <svg width="24" height="24" viewBox="0 0 24 24"><circle cx="12" cy="12" r="10.5" fill="#eee" stroke="#666" stroke-width="2"/><path d="M12 6v6l4 3" stroke="#444" stroke-width="1.8" fill="none"/></svg>Posted 17. Aug, 2012
    </div>
  </article>
  <article class="job" style="left:453px;top:823px">
    <h3>Sales Consultants</h3>
    <p>We have a variety of locations around the UK where we are looking to p...</p>
    <div class="job-meta">
      <svg width="14" height="20" viewBox="0 0 14 20"><path d="M7 20C3 14 0 10 0 7a7 7 0 0 1 14 0c0 3-3 7-7 13z" fill="#e0502a"/><circle cx="7" cy="7" r="2.5" fill="#fff"/></svg>Where it is?<span class="gap"></span>
      <svg width="24" height="24" viewBox="0 0 24 24"><circle cx="12" cy="12" r="10.5" fill="#eee" stroke="#666" stroke-width="2"/><path d="M12 6v6l4 3" stroke="#444" stroke-width="1.8" fill="none"/></svg>Posted 11. Oct, 2012
    </div>
  </article>
  <article class="job" style="left:161px;top:939px">
    <h3>Groom</h3>
    <p>General upkeep of stable yard and grooming and feeding of horses and y...</p>
    <div class="job-meta">
      <svg width="14" height="20" viewBox="0 0 14 20"><path d="M7 20C3 14 0 10 0 7a7 7 0 0 1 14 0c0 3-3 7-7 13z" fill="#e0502a"/><circle cx="7" cy="7" r="2.5" fill="#fff"/></svg>Where it is?<span class="gap"></span>
      <svg width="24" height="24" viewBox="0 0 24 24"><circle cx="12" cy="12" r="10.5" fill="#eee" stroke="#666" stroke-width="2"/><path d="M12 6v6l4 3" stroke="#444" stroke-width="1.8" fill="none"/></svg>Posted 18. Jul, 2012
    </div>
  </article>
  <article class="job" style="left:453px;top:939px">
    <h3>Polo Groom</h3>
    <p>Looking after our clients polo ponies to a very high standard. Horses ...</p>
    <div class="job-meta">
      <svg width="14" height="20" viewBox="0 0 14 20"><path d="M7 20C3 14 0 10 0 7a7 7 0 0 1 14 0c0 3-3 7-7 13z" fill="#e0502a"/><circle cx="7" cy="7" r="2.5" fill="#fff"/></svg>Where it is?<span class="gap"></span>
      <svg width="24" height="24" viewBox="0 0 24 24"><circle cx="12" cy="12" r="10.5" fill="#eee" stroke="#666" stroke-width="2"/><path d="M12 6v6l4 3" stroke="#444" stroke-width="1.8" fill="none"/></svg>Posted 9. May, 2012
    </div>
  </article>

  <h2 class="section-title" style="left:786px;top:758px">Current CV's</h2>
  <table class="cv-table">
    <colgroup><col style="width:85px"><col style="width:140px"><col style="width:53px"><col style="width:70px"></colgroup>
    <tr><th>Name</th><th>Title</th><th>View</th><th>Delete</th></tr>
    <tr><td>john</td><td class="file">john_cv.docx</td><td class="icon"><svg width="26" height="16" viewBox="0 0 26 16"><ellipse cx="13" cy="8" rx="12" ry="7" fill="#8a8a8a"/><circle cx="13" cy="8" r="4" fill="#eee"/><circle cx="13" cy="8" r="2" fill="#8a8a8a"/></svg></td><td class="icon"><svg width="16" height="18" viewBox="0 0 16 18"><rect x="1" y="2" width="14" height="2" fill="#8aa0b5"/><rect x="6" y="0" width="4" height="2" fill="#8aa0b5"/><path d="M3 5h10l-1 12H4z" fill="none" stroke="#8aa0b5" stroke-width="1.5"/><path d="M6.5 7v8M9.5 7v8" stroke="#8aa0b5"/></svg></td></tr>
    <tr><td>john</td><td class="file">john_cv.docx</td><td class="icon"><svg width="26" height="16" viewBox="0 0 26 16"><ellipse cx="13" cy="8" rx="12" ry="7" fill="#8a8a8a"/><circle cx="13" cy="8" r="4" fill="#eee"/><circle cx="13" cy="8" r="2" fill="#8a8a8a"/></svg></td><td class="icon"><svg width="16" height="18" viewBox="0 0 16 18"><rect x="1" y="2" width="14" height="2" fill="#8aa0b5"/><rect x="6" y="0" width="4" height="2" fill="#8aa0b5"/><path d="M3 5h10l-1 12H4z" fill="none" stroke="#8aa0b5" stroke-width="1.5"/><path d="M6.5 7v8M9.5 7v8" stroke="#8aa0b5"/></svg></td></tr>
    <tr><td>john</td><td class="file">john_cv.docx</td><td class="icon"><svg width="26" height="16" viewBox="0 0 26 16"><ellipse cx="13" cy="8" rx="12" ry="7" fill="#8a8a8a"/><circle cx="13" cy="8" r="4" fill="#eee"/><circle cx="13" cy="8" r="2" fill="#8a8a8a"/></svg></td><td class="icon"><svg width="16" height="18" viewBox="0 0 16 18"><rect x="1" y="2" width="14" height="2" fill="#8aa0b5"/><rect x="6" y="0" width="4" height="2" fill="#8aa0b5"/><path d="M3 5h10l-1 12H4z" fill="none" stroke="#8aa0b5" stroke-width="1.5"/><path d="M6.5 7v8M9.5 7v8" stroke="#8aa0b5"/></svg></td></tr>
    <tr><td>john</td><td class="file">john_cv.docx</td><td class="icon"><svg width="26" height="16" viewBox="0 0 26 16"><ellipse cx="13" cy="8" rx="12" ry="7" fill="#8a8a8a"/><circle cx="13" cy="8" r="4" fill="#eee"/><circle cx="13" cy="8" r="2" fill="#8a8a8a"/></svg></td><td class="icon"><svg width="16" height="18" viewBox="0 0 16 18"><rect x="1" y="2" width="14" height="2" fill="#8aa0b5"/><rect x="6" y="0" width="4" height="2" fill="#8aa0b5"/><path d="M3 5h10l-1 12H4z" fill="none" stroke="#8aa0b5" stroke-width="1.5"/><path d="M6.5 7v8M9.5 7v8" stroke="#8aa0b5"/></svg></td></tr>
    <tr><td>john</td><td class="file">john_cv.docx</td><td class="icon"><svg width="26" height="16" viewBox="0 0 26 16"><ellipse cx="13" cy="8" rx="12" ry="7" fill="#8a8a8a"/><circle cx="13" cy="8" r="4" fill="#eee"/><circle cx="13" cy="8" r="2" fill="#8a8a8a"/></svg></td><td class="icon"><svg width="16" height="18" viewBox="0 0 16 18"><rect x="1" y="2" width="14" height="2" fill="#8aa0b5"/><rect x="6" y="0" width="4" height="2" fill="#8aa0b5"/><path d="M3 5h10l-1 12H4z" fill="none" stroke="#8aa0b5" stroke-width="1.5"/><path d="M6.5 7v8M9.5 7v8" stroke="#8aa0b5"/></svg></td></tr>
  </table>

  <!-- partners -->
  <section class="partners"></section>
  <svg class="abs" style="left:139px;top:1073px" width="32" height="32" viewBox="0 0 32 32"><circle cx="16" cy="16" r="14" fill="#fff" stroke="#111" stroke-width="3"/><path d="M19 9l-7 7 7 7" stroke="#111" stroke-width="3.5" fill="none"/></svg>
  <span class="partner" style="left:205px">hireharbour.co.uk</span>
  <span class="partner" style="left:362px;font-size:12px;top:1083px">shoproles.co.uk</span>
  <span class="partner" style="left:513px;color:#222">TechPost Board.co.uk</span>
  <span class="partner" style="left:669px;font-size:13px;top:1081px">BuildRoles Search</span>
  <span class="partner" style="left:815px">hireharbour.co.uk</span>
  <span class="partner" style="left:972px;font-size:12px;top:1083px">shoproles.co.uk</span>
  <svg class="abs" style="left:1109px;top:1073px" width="32" height="32" viewBox="0 0 32 32"><circle cx="16" cy="16" r="14" fill="#fff" stroke="#111" stroke-width="3"/><path d="M13 9l7 7-7 7" stroke="#111" stroke-width="3.5" fill="none"/></svg>

  <!-- footer -->
  <footer class="site-footer"></footer>
  <div class="rule-v" style="left:319px;top:1127px;height:258px;border-color:#3a3a3a"></div>
  <div class="rule-v" style="left:625px;top:1127px;height:258px;border-color:#3a3a3a"></div>
  <div class="rule-v" style="left:814px;top:1127px;height:258px;border-color:#3a3a3a"></div>

  <h4 class="foot-title" style="left:140px">Navigation</h4>
  <ul class="foot-list" style="left:140px;top:1203px">
    <li><svg width="13" height="13" viewBox="0 0 13 13"><circle cx="6.5" cy="6.5" r="5.5" fill="none" stroke="#666"/><path d="M5 4l3 2.5L5 9" stroke="#666" fill="none"/></svg>Home</li>
    <li><svg width="13" height="13" viewBox="0 0 13 13"><circle cx="6.5" cy="6.5" r="5.5" fill="none" stroke="#666"/><path d="M5 4l3 2.5L5 9" stroke="#666" fill="none"/></svg>About Paddock Crew</li>
    <li><svg width="13" height="13" viewBox="0 0 13 13"><circle cx="6.5" cy="6.5" r="5.5" fill="none" stroke="#666"/><path d="M5 4l3 2.5L5 9" stroke="#666" fill="none"/></svg>Equine Job Seekers</li>
    <li><svg width="13" height="13" viewBox="0 0 13 13"><circle cx="6.5" cy="6.5" r="5.5" fill="none" stroke="#666"/><path d="M5 4l3 2.5L5 9" stroke="#666" fill="none"/></svg>Equine Employers</li>
    <li><svg width="13" height="13" viewBox="0 0 13 13"><circle cx="6.5" cy="6.5" r="5.5" fill="none" stroke="#666"/><path d="M5 4l3 2.5L5 9" stroke="#666" fill="none"/></svg>Equine Industry News</li>
    <li><svg width="13" height="13" viewBox="0 0 13 13"><circle cx="6.5" cy="6.5" r="5.5" fill="none" stroke="#666"/><path d="M5 4l3 2.5L5 9" stroke="#666" fill="none"/></svg>Equestrian Resources</li>
    <li><svg width="13" height="13" viewBox="0 0 13 13"><circle cx="6.5" cy="6.5" r="5.5" fill="none" stroke="#666"/><path d="M5 4l3 2.5L5 9" stroke="#666" fill="none"/></svg>Webmasters</li>
    <li><svg width="13" height="13" viewBox="0 0 13 13"><circle cx="6.5" cy="6.5" r="5.5" fill="none" stroke="#666"/><path d="M5 4l3 2.5L5 9" stroke="#666" fill="none"/></svg>Login</li>
    <li><svg width="13" height="13" viewBox="0 0 13 13"><circle cx="6.5" cy="6.5" r="5.5" fill="none" stroke="#666"/><path d="M5 4l3 2.5L5 9" stroke="#666" fill="none"/></svg>Sitemap</li>
  </ul>

  <h4 class="foot-title" style="left:356px">Newsletter Sign Up</h4>
  <span class="foot-label">Enter your Email Address</span>
  <div class="foot-field">Email</div>
  <div class="btn btn-dark" style="left:355px;top:1277px;width:127px;height:36px;line-height:35px">Sign Up!</div>

  <h4 class="foot-title" style="left:659px">Social Media</h4>
  <ul class="foot-list social" style="left:659px;top:1205px">
    <li><span class="sq" style="background:#3b5a98"></span>Friendbook</li>
    <li><span class="sq" style="background:#3fa9e0"></span>Chirper</li>
    <li><span class="sq" style="background:#1c7ab3"></span>LinkLine</li>
    <li><span class="sq" style="background:#f08a1c"></span>Rss</li>
  </ul>

  <h4 class="foot-title" style="left:853px">Testimonials</h4>
  <div class="quote">Lorem ipsum dolor sit amet, consectetur adipisicing elit, sed do eiusmod tempor incididunt ut &nbsp;labore et dolore magna aliqua. Lorem ipsum dolor sit amet, consectetur adipisicing elit, sed do eiusmod tempor incididunt ut &nbsp;labore et dolore magna aliqua.</div>
  <svg class="abs" style="left:1072px;top:1338px" width="50" height="26" viewBox="0 0 50 26"><path d="M18 0h30L2 26z" fill="#5e9c0f"/></svg>
  <span class="quote-author">Martin Coleby, Ridgefield Ltd</span>

  <div class="copy-bar">Copyright © 2012 PaddockCrew. All rights reserved!</div>
</div>
</body>
</html>
```